Packaging Design for a wafer product

Dorvenn is a leading chocolate manufacturer in Zimbabwe. Dorvenn is lauching a wafer product with layers of delicious Dorvenn chocolate in between. The product will be called Mokarund. The pack will be a six colour design printed on metallised polypropelene. We attach a photo of the product as well as photos of the existing chocolate portfolio to guide the designers. The design must be bright and appealing

Manufacturer

```html
<!DOCTYPE html>
<html lang="en">
<head>
<meta charset="utf-8">
<title>Mokarund Wafer Pack</title>
<link href="https://fonts.googleapis.com/css2?family=Oswald:wght@500;700&display=swap" rel="stylesheet">
<style>
  :root {
    --paper: #ffffff;
    --choc: #8b5a2f;
    --choc-dark: #5e3718;
    --choc-end: #7a4822;
    --caramel: #c88a4f;
    --caramel-light: #e0ad73;
    --purple: #4f3584;
    --purple-light: #6b4fa6;
    --cream: #fdf6ec;
    --ink: #3a2210;
  }
  html, body { margin: 0; padding: 0; overflow: hidden; }
  body { width: 849px; height: 1200px; background: var(--paper); position: relative; font-family: "Oswald", sans-serif; }
  .pack { position: absolute; left: 0; top: 0; width: 849px; height: 1200px; }
  .pack-art { position: absolute; left: 0; top: 0; }
  .logo-spot {
    position: absolute; left: 128px; top: 566px; width: 62px; height: 62px;
    border-radius: 50%; background: var(--cream);
    display: flex; align-items: center; justify-content: center;
    font-family: "Oswald", sans-serif; font-weight: 500; font-size: 22px; color: var(--ink);
  }
  .flavour-badge {
    position: absolute; left: 360px; top: 488px; width: 108px; height: 30px;
    background: var(--purple); transform: rotate(-8deg);
    display: flex; align-items: center; justify-content: center;
    border: 2px solid var(--cream);
  }
  .flavour-badge span {
    font-family: "Oswald", sans-serif; font-weight: 500; font-size: 15px; color: var(--cream);
  }
  .brand-name {
    position: absolute; left: 300px; top: 572px; width: 230px; text-align: center;
    font-family: "Oswald", sans-serif; font-weight: 700; font-size: 56px; line-height: 1;
    color: var(--cream); margin: 0;
  }
  .tagline {
    position: absolute; left: 300px; top: 640px; width: 230px; text-align: center;
    font-family: "Oswald", sans-serif; font-weight: 500; font-size: 22px; line-height: 1;
    color: var(--cream); margin: 0;
  }
  .net-weight {
    position: absolute; left: 118px; top: 720px;
    font-family: "Oswald", sans-serif; font-weight: 500; font-size: 17px; color: var(--cream);
  }
</style>
</head>
<body>
<div class="pack">
  <svg class="pack-art" width="849" height="1200" viewBox="0 0 849 1200" xmlns="http://www.w3.org/2000/svg">
    <defs>
      <linearGradient id="bodyShade" x1="0" y1="0" x2="0" y2="1">
        <stop offset="0" stop-color="#9a673a"/>
        <stop offset="1" stop-color="#7d4f28"/>
      </linearGradient>
      <linearGradient id="waferFill" x1="0" y1="0" x2="1" y2="1">
        <stop offset="0" stop-color="#8a5530"/>
        <stop offset="1" stop-color="#4a2812"/>
      </linearGradient>
    </defs>
    <!-- crimped ends -->
    <path class="crimp-left" fill="var(--choc-end)"
      d="M105 488 L44 496 L56 512 L44 528 L56 544 L44 560 L56 576 L44 592 L56 608 L44 624 L56 640 L44 656 L56 672 L44 688 L56 704 L44 720 L56 736 L44 748 L105 752 Z"/>
    <path class="crimp-right" fill="var(--choc-end)"
      d="M744 488 L805 496 L793 512 L805 528 L793 544 L805 560 L793 576 L805 592 L793 608 L805 624 L793 640 L805 656 L793 672 L805 688 L793 704 L805 720 L793 736 L805 748 L744 752 Z"/>
    <!-- wrapper body -->
    <rect class="wrapper-body" x="100" y="485" width="649" height="268" fill="url(#bodyShade)"/>
    <!-- caramel swoosh -->
    <path class="swoosh" fill="var(--caramel)" opacity="0.85"
      d="M100 610 C260 560 420 560 560 600 C640 622 700 612 749 590 L749 690 C620 720 460 690 320 680 C220 672 160 690 100 705 Z"/>
    <path class="swoosh-light" fill="var(--caramel-light)" opacity="0.5"
      d="M100 640 C240 600 400 610 520 640 C600 660 680 650 749 630 L749 660 C650 690 540 680 430 662 C300 645 200 660 100 680 Z"/>
    <!-- purple band -->
    <path class="purple-band" fill="var(--purple)"
      d="M100 700 C260 676 440 688 560 700 C640 708 700 700 749 688 L749 722 C660 736 560 730 440 722 C300 714 190 718 100 732 Z"/>
    <path class="purple-band-light" fill="var(--purple-light)"
      d="M100 732 C200 718 320 716 440 722 C560 730 660 736 749 722 L749 736 C640 748 520 742 400 736 C280 730 180 736 100 746 Z"/>
    <!-- small wafer mark beside the name -->
    <rect role="img" aria-label="Small wafer bites icon" x="270" y="560" width="34" height="30" rx="4" fill="var(--cream)" opacity="0.9"/>
    <!-- wafer product illustration area -->
    <rect role="img" aria-label="Chocolate wafer bars with a bite taken out" x="548" y="576" width="186" height="142" rx="6" fill="url(#waferFill)"/>
  </svg>

  <div class="logo-spot">logo</div>
  <div class="flavour-badge"><span>New flavour</span></div>
  <h1 class="brand-name">Mokarund</h1>
  <p class="tagline">Take your bite</p>
  <div class="net-weight">40g</div>
</div>
</body>
</html>
```